Trade Alert Service needs Youtube thumbnail / channel design

I'm about to set up a Youtube channel which gives real-time trade alerts to earn passive income. I'm looking for a Youtube channel design to include thumbnail and other associated visuals for the channel.
The trade alerts will be focused around selling cash-secured put options on US equities, and directed at people who want investing advice / tips for getting out of the rat race. I'd like the theme to be somewhat serious / credible, without too many eye-popping neon colours like all the other cheap trade alert videos / day trading videos on Youtube. Happy for you to use your experience if you think otherwise though, as you're the designer, not me!

Target Market(s)

Option Traders, Value Investors, People who want passive income

Industry/Entity Type

Finance

Logo Text

Bramblewick Quarter Guild

Requirements
Must have
• All relevant Youtube visuals so that I can upload them to the Youtube channel - all visuals required by Youtube Studio upload within the channel creation page.
A logo so that I can append it to Powerpoint presentations
Nice to have
• A blank Powerpoint slide template showing the logo would be great in chosen colour scheme

```html
<!DOCTYPE html>
<html lang="en">
<head>
<meta charset="utf-8">
<title>Bramblewick Quarter Guild — Trading and Investing Our Way to Financial Freedom</title>
<link rel="stylesheet" href="https://fonts.googleapis.com/css2?family=League+Spartan:wght@600;700&display=swap">
<style>
  :root {
    --indigo: #30009a;
    --white: #ffffff;
    --gold: #fcd22a;
    --photo-warm: #e8643f;
    --photo-pale: #d9cde8;
    --photo-lilac: #b7a3d8;
    --icon-red: #f2384f;
    --icon-pink: #e94fa0;
    --icon-blue: #49c6ef;
  }
  * { margin: 0; padding: 0; box-sizing: border-box; }
  html, body { width: 1200px; height: 675px; overflow: hidden; background: var(--indigo); }
  .thumbnail {
    position: relative;
    width: 1200px;
    height: 675px;
    background: var(--indigo);
    font-family: "League Spartan", "Montserrat", sans-serif;
    color: var(--white);
    overflow: hidden;
  }
  .desk-photo {
    position: absolute;
    left: 0; top: 0;
    width: 1200px; height: 214px;
    background:
      linear-gradient(180deg, rgba(48,0,154,0.18), rgba(48,0,154,0.28)),
      linear-gradient(90deg, var(--photo-warm) 0%, #d97a6a 28%, var(--photo-lilac) 52%, var(--photo-pale) 75%, #cbbfe3 100%);
  }
  .accent-rule {
    position: absolute;
    left: 52px; top: 0;
    width: 16px; height: 675px;
    background: var(--gold);
  }
  .headline {
    position: absolute;
    left: 113px; top: 252px;
    font-size: 83px;
    font-weight: 700;
    line-height: 94px;
    letter-spacing: 0.02em;
    text-transform: uppercase;
  }
  .tagline {
    position: absolute;
    left: 115px; top: 540px;
    font-size: 35px;
    font-weight: 600;
    line-height: 43px;
    letter-spacing: 0.155em;
    text-transform: uppercase;
    white-space: nowrap;
  }
  .settings-icon {
    position: absolute;
    left: 830px; top: 305px;
    width: 290px; height: 268px;
    border-radius: 18px;
    background: linear-gradient(180deg, var(--icon-red) 0%, var(--icon-pink) 50%, var(--icon-blue) 100%);
    opacity: 0.35;
  }
</style>
</head>
<body>
<main class="thumbnail">
  <div class="desk-photo" role="img" aria-label="Close-up of a hand resting on a printed financial report with bar and pie charts beside an orange coffee cup"></div>
  <div class="accent-rule"></div>

  <h1 class="headline">Bramblewick<br>Quarter<br>Guild</h1>
  <p class="tagline">Trading and investing our<br>way to financial freedom</p>

  <div class="settings-icon" role="img" aria-label="Line icon of a folder with a settings gear, drawn in a red to pink to blue gradient"></div>
</main>
</body>
</html>
```